Superfood Organic Powder needs a new Standup Pouch Design

Superfood brand needs a new package design Standup pouch

We need a new packaging design
*Standup Pouch*
for a NEW superfood product to our brand PureLeafy.

This product is a superfood blend of organic powders such as spiralina, chlorella, wheatgrass etc.

The design should be modern with an organic look, - but feel free to play around with it as you wish.

Our first or *older* product is called Vital Sprout, and contains superfood powders like Maca, Moringa, Baobab, Spirulina, Chlorella, Wheatgrass

Find measurements for the standup pouch in the attachments.

We can either go with a

a white standup pouch with a slight opacity to it
(see attached sample I have from my supplier)

or

mat white standup pouch

Or Natural Kraft if

The white pouch with a slight opacity to it so you can see the powder through the pouch. One cool thing about this one is that if we have an area in the design with no colors, not even white, that area will be completely transparent, see picture of the sample pouch we have in the attachments.
In the sample photo the spider is completely transparent.

The Mat white pouch is just a basic white standup pouch with a mat finish.
What ever you think is best for your design you can suggest.

In the future we will create multiple products, each product should have its own color style to distinguish between them - this product should use green Color code as one of the green colors used in the logo. Of course not all colors should have that code, but just the identifier for this product. Please present an idea to showcase this identifier, it could be a thick horizontal or vertical line somewhere on the pouch.

The standup pouch will be digitally printed so we can use all areas of the pouch.

Please provide 3D mockup of the design in order to better get an idea of the design.
Remember that I consider you as the expert so I'm very open to any suggestions regarding this design - in the end the main goal is to attract customers and that is your area of expertise.

Please let me know if you have any questions - thanks in advance

I'm looking forward to working with you.

Here are some links I have found that I think is great designs just to give a little insight to my designs wishes.:

https://www.pinboardia.dk/pin/603918274615093821/ https://www.verdantmeadowfoods.com/collections/all-superfood-products
https://www.pinboardia.dk/pin/482710395627184039/
https://draftarena.dk/product-label-design/contests/print-design-stand-up-resealable-pouch-organic-spice-571036
https://www.pinboardia.dk/pin/738162940571836204/
https://www.pinboardia.dk/pin/27640918365201478/
https://www.pinboardia.dk/pin/619384027516293847/
https://www.pinboardia.dk/pin/857302619483027164/ https://www.pinboardia.dk/pin/364817502938471620/
https://www.pinboardia.dk/pin/93827405162938471/

Target Market(s)

Vegans, Organic interested clients, healthy living, Fitness, Juicers

Industry/Entity Type

Health And Wellness

Requirements
Must have
• The following text should be added on front of the label under the product name:
• Danish certified organic
• Superfood blend
• —
• The product contains the following ingredients and should be mentioned on the front - only the ingredients names:
• Maca, Moringa, Baobab, Spirulina, Chlorella, Wheatgrass
• —
• Organic logo:
• Organic EU logo should be present on the back (find logo in the attachments) To the right of the logo the following text is mandatory with Myriad Pro Regular as a type-font: See previous design for instructions.
• "EU-LOGO-HERE"
• DK-ØKO-100
• EU/ikke-EU-jordbrug
• EU/non-EU Agriculture
• Next to the EU organic logo we will place the danish organic logo which is attached as well, you can decide if it should be on the left or right side, it is a red Ø logo ( find in the attachments as well.
• —
• The label should contain a Nutritional Information with the danish language as primary. By law in Denmark the language used should be danish but it is allowed to add the English word after the danish separated by a /
• So it should be titled as Næringsindhold / Nutritional information (Title Bold font)
• And contain the following:
• energi (KJ/kcal)
• • fedt / fat (g)
• • - heraf mættede fedtsyrer / from saturated fat (g)
• • kulhydrat / carbohydrates (g)
• • - heraf sukkerarter / from sugar (g)
• • protein (g)
• • salt (g)
• • kostfibre / dietary fiber (g)
• —
• We need ingredients list on the back as well titled Ingredienser / Ingredients (Title Bold font)
• Maca, Moringa, Baobab, Spirulina, Chlorella, Hvedegræs / Wheatgrass
• Nettovægt / Netto weight 225 gr
• —-
• You can add some cool logos indicating that the product is:
• 100 % organic
• 100% vegan
• No additives
• Non-GMO
• Gluten free
• —
• Instructions (Title Bold font)
• Mix the superfood powder into 250 ml water with a twist of lemon, coconut water, green juice, smoothies, almond milk, or add to your favorit morning meal.
• Serving size 1-2 teaspoon
• Would be great with 3-4 images describing the instructions
• Image 1 could be fruit being put in a blender
• Image 2 could be 1 teaspoon with powder on top of a blender
• Image 3 could be a blender in use
• Image 4 poring the smoothie in to a glass to enjoy
• —
• Opbevaring / Storage (Title Bold font)
• Opbevares tørt og ikke for varmt
• Keep in a cool and dry place away from sunlight
• —
• Batch: (Title Bold font)
• Best before / Bedst før: (Title Bold font)
• —
• Barcode field
• Make room for a barcode
• —
• Produced in EU for: (Title Bold font)
• Solbrink IVS
• Lærkevænget 42
• 7730 Hørbyvig N
• Denmark
• www.pureleafy.eu (make this bold as well)
• —
• Follow us (Title Bold font)
• Instagram and facebook logo on the back with hashtag #pureleafyeu
• —
• Other than that pureleafy logo can be added as well, it is attached as well.
• I will attach our logo with original AI files.
• —
• Our mission (text)
• We want to provide our customers with the best possible superfood blends. Allowing our customers to get a product packed with antioxidants, vitamins and minerals to elevate their health to the next level. All our products are vegan friendly and GMO free - produced under the best possible circumstances.
• —
Nice to have
• Green color from the logo can be used to get it streamlined.
• Color code c2ce48

```html
<!DOCTYPE html>
<html lang="en">
<head>
<meta charset="utf-8">
<title>PureLeafy – Vital Sprout Standup Pouch</title>
<link rel="stylesheet" href="https://fonts.googleapis.com/css2?family=Raleway:wght@400;500;800&family=Great+Vibes&family=Oswald:wght@500&display=swap">
<style>
  :root {
    --stage: #e6e7e3;
    --pouch: #ffffff;
    --identifier: #c2ce48;
    --band: #a9bc34;
    --band-deep: #93a52a;
    --brand-green: #1f9e2f;
    --deep-green: #2d6b22;
    --leaf-light: #9cc83a;
    --leaf-mid: #6fa522;
    --leaf-dark: #3f7d14;
    --sketch: #e4ebc2;
    --seal-red: #c8202a;
    --white: #ffffff;
  }
  * { margin: 0; padding: 0; box-sizing: border-box; }
  html, body { width: 1200px; height: 1147px; overflow: hidden; background: var(--stage); }
  .pouch-front {
    position: absolute; left: 235px; top: 0;
    width: 730px; height: 1147px;
    background: var(--pouch);
    overflow: hidden;
    font-family: "Raleway", sans-serif;
  }
  .product-band {
    position: absolute; left: 99px; top: 0; width: 139px; height: 284px;
    background: var(--band);
    clip-path: polygon(0 0, 100% 0, 100% 96%, 50% 100%, 0 96%);
  }
  .product-band .vegan {
    position: absolute; top: 44px; width: 100%; text-align: center;
    font-family: "Great Vibes", cursive; font-size: 38px; color: var(--white);
  }
  .product-band .dots {
    position: absolute; left: 12px; right: 12px; top: 108px;
    border-top: 2px dotted rgba(255,255,255,.8);
  }
  .product-band .badge {
    position: absolute; left: 8px; right: 8px; top: 124px; bottom: 14px;
    background: var(--band-deep); border-radius: 10px 10px 4px 4px;
  }
  .product-band .badge::after {
    content: ""; position: absolute; left: 50%; top: 50%;
    width: 86px; height: 86px; margin: -43px 0 0 -43px;
    border-radius: 50%; border: 3px solid rgba(255,255,255,.55);
  }
  .brand {
    position: absolute; left: 419px; top: 250px; width: 262px; text-align: center;
  }
  .brand .dot {
    width: 70px; height: 70px; border-radius: 50%;
    background: var(--identifier); margin: 0 auto 18px;
  }
  .brand .name {
    font-size: 50px; font-weight: 500; color: var(--brand-green); letter-spacing: 1px;
  }
  .divider {
    position: absolute; left: 433px; top: 458px; width: 234px; height: 2px;
    background: var(--brand-green);
  }
  .claim { position: absolute; left: 419px; width: 262px; text-align: center; color: var(--brand-green); }
  .claim.certified { top: 478px; font-size: 26px; font-weight: 400; letter-spacing: .3px; }
  .claim.organic { top: 506px; font-size: 52px; font-weight: 500; letter-spacing: 1px; line-height: 1; }
  .claim.blend { top: 560px; font-family: "Great Vibes", cursive; font-size: 30px; color: var(--deep-green); }
  .leaf-art {
    position: absolute; left: 50px; top: 375px; width: 300px; height: 440px;
    border-radius: 120px 30px 120px 30px;
    background:
      radial-gradient(ellipse 45% 30% at 30% 22%, var(--leaf-light), transparent 70%),
      radial-gradient(ellipse 45% 35% at 72% 40%, var(--leaf-light), transparent 70%),
      radial-gradient(ellipse 45% 35% at 35% 62%, var(--leaf-mid), transparent 72%),
      radial-gradient(ellipse 45% 35% at 70% 82%, var(--leaf-mid), transparent 72%),
      linear-gradient(160deg, var(--leaf-mid), var(--leaf-dark));
  }
  .sketch-art {
    position: absolute; left: 50px; top: 815px; width: 340px; height: 332px;
    background:
      radial-gradient(ellipse 40% 30% at 30% 20%, var(--sketch), transparent 75%),
      radial-gradient(ellipse 35% 25% at 60% 55%, var(--sketch), transparent 75%),
      radial-gradient(ellipse 45% 30% at 45% 90%, var(--sketch), transparent 75%),
      linear-gradient(180deg, #f4f7e6, #fbfcf5);
    border-radius: 24px 24px 0 0;
  }
  .organic-seal {
    position: absolute; left: 85px; top: 1045px; width: 56px; height: 56px;
    border-radius: 50%; background: var(--seal-red);
  }
  .identifier-panel {
    position: absolute; left: 374px; top: 648px; width: 356px; height: 325px;
    background: var(--identifier); border-radius: 18px 0 0 18px;
    color: var(--white);
  }
  .identifier-panel .title { position: absolute; left: 42px; top: 28px; line-height: .95; }
  .identifier-panel .title .top { display: block; font-size: 72px; font-weight: 800; }
  .identifier-panel .title .bottom { display: block; font-size: 62px; font-weight: 400; letter-spacing: 1px; }
  .identifier-panel .rule {
    position: absolute; left: 42px; right: 46px; border-top: 2px dotted rgba(255,255,255,.85);
  }
  .identifier-panel .rule.upper { top: 180px; }
  .identifier-panel .rule.lower { top: 240px; }
  .claims {
    position: absolute; left: 42px; right: 46px; top: 190px;
    display: flex; justify-content: space-between; list-style: none;
  }
  .claims li {
    flex: 1; text-align: center; border-left: 1px solid rgba(255,255,255,.85);
  }
  .claims li:first-child { border-left: none; text-align: left; }
  .claims b { display: block; font-size: 16px; font-weight: 500; }
  .claims span { display: block; font-size: 11px; margin-top: 4px; color: #3c4a10; }
  .ingredients {
    position: absolute; left: 42px; top: 270px; width: 260px;
    font-family: "Oswald", sans-serif; font-size: 11px; line-height: 1.45;
    text-transform: uppercase; letter-spacing: .2px;
  }
</style>
</head>
<body>
  <main class="pouch-front">
    <div class="product-band">
      <div class="vegan">Vegan</div>
      <div class="dots"></div>
      <div class="badge" role="img" aria-label="Certified gluten-free badge"></div>
    </div>

    <div class="brand">
      <div class="dot"></div>
      <div class="name">PureLeafy</div>
    </div>
    <div class="divider"></div>
    <p class="claim certified">DANISH CERTIFIED</p>
    <p class="claim organic">ORGANIC</p>
    <p class="claim blend">Superfood Blend</p>

    <div class="sketch-art" role="img" aria-label="Light line sketches of falling leaves"></div>
    <div class="leaf-art" role="img" aria-label="Cluster of four green leaf shapes filled with green powder texture"></div>
    <div class="organic-seal" role="img" aria-label="Danish state-controlled organic seal"></div>

    <section class="identifier-panel">
      <h1 class="title"><span class="top">VITAL</span><span class="bottom">SPROUT</span></h1>
      <div class="rule upper"></div>
      <ul class="claims">
        <li><b>100 %</b><span>Organic</span></li>
        <li><b>100 %</b><span>Vegan</span></li>
        <li><b>NO</b><span>Additives</span></li>
        <li><b>NON</b><span>GMO</span></li>
      </ul>
      <div class="rule lower"></div>
      <p class="ingredients">Maca, Moringa, Baobab,<br>Spirulina, Chlorella, Wheatgrass</p>
    </section>
  </main>
</body>
</html>
```